Banner Ad Design Project

I need a banner design. The website is under construction at www.brightmarrowfield.com

Name: Bright Marrow
Tagline: Leadership Inspiration for busy people

This is a leadership development and executive coaching site. The past site is live at www.quillponderhub.com. (so you can get a sense of the content)

The audience are (BUSY) executives, senior managers, leaders and top professionals, so the feel needs to be highly professional but also modern and fresh. I want to communicate energy but also solid and trust worthy and not too new agey. The audience are also people with strong social values who want to change things - so not too corporate (Ie suits!)

I would like the design to be floating on a white background, very clean and simple. I am attracted to reds or sunset (burn orange crimson colors.) But totally open to any color ideas.
I am giving an open brief for your ideas.
Here are the dimensions 960px wide, roughly 190px height.
Updates

Project Deadline Extended
Reason: The weekend might give more time to designers to get involved. Thanks Mirel

Hi designers

You may not have seen the additions I gave to this brief.

The banner should not have leader out front photo's. Maybe less corporate than I initially thought. 
Not too corporate (no suits!) Please no chess pieces, jigsaw pieces, cartoon images, cliche leadership images. 
Am am trying for inspiration /inspiring whilst still being professional. Very simple and clean.
Please can the design be floating in a white background so that the web page is borderless - A bit like it is in http://tamberwickcove.com/
Thank you

Target Market(s)

Senior managers, executives but people who also want to change the world!

Industry/Entity Type

Construction

Requirements
Should not have
• Should not have leader out front photo's.
Maybe less corporate than I initially thought.
Am am trying for inspiration /inspiring whilst still being professional.
Please no chess pieces, jigsaw pieces, cartoon images, cliche leadership images. Not too corporate (Ie suits!)

Thanks

```html
<!DOCTYPE html>
<html lang="en">
<head>
<meta charset="utf-8">
<title>Bright Marrow — Rise Above</title>
<link rel="stylesheet" href="https://fonts.googleapis.com/css2?family=Tenor+Sans&display=swap">
<style>
  :root {
    --canvas-bg: #ffffff;
    --brand-red: #c9343d;
    --tagline-brown: #8c6b60;
    --blossom-pink: #f2a9b0;
    --blossom-light: #fbe3e4;
  }
  html, body {
    margin: 0;
    padding: 0;
    width: 1200px;
    height: 238px;
    overflow: hidden;
    background: var(--canvas-bg);
  }
  .banner {
    position: relative;
    width: 1200px;
    height: 238px;
    background: var(--canvas-bg);
    overflow: hidden;
  }
  .brand-name {
    position: absolute;
    left: 46px;
    top: 24px;
    margin: 0;
    font-family: "Tenor Sans", sans-serif;
    font-weight: 400;
    font-size: 104px;
    line-height: 1.2;
    color: var(--brand-red);
    letter-spacing: 0;
    white-space: nowrap;
  }
  .tagline {
    position: absolute;
    left: 56px;
    top: 170px;
    margin: 0;
    font-family: "Tenor Sans", sans-serif;
    font-size: 22px;
    line-height: 1;
    color: var(--tagline-brown);
    letter-spacing: 0.95em;
    text-transform: uppercase;
    white-space: nowrap;
  }
  .blossom-branch {
    position: absolute;
    left: 790px;
    top: 24px;
    width: 410px;
    height: 186px;
  }
</style>
</head>
<body>
  <main class="banner">
    <h1 class="brand-name">Bright Marrow</h1>
    <p class="tagline">Rise Above . . .</p>
    <svg class="blossom-branch" viewBox="0 0 410 186" role="img" aria-label="Photograph of a branch of pink cherry blossoms on white">
      <defs>
        <radialGradient id="blossom-glow" cx="50%" cy="45%" r="60%">
          <stop offset="0%" stop-color="#f2a9b0" stop-opacity="0.85"/>
          <stop offset="60%" stop-color="#fbe3e4" stop-opacity="0.7"/>
          <stop offset="100%" stop-color="#ffffff" stop-opacity="0"/>
        </radialGradient>
      </defs>
      <ellipse cx="205" cy="93" rx="205" ry="93" fill="url(#blossom-glow)"/>
    </svg>
  </main>
</body>
</html>
```